Gardener needs an exciting new flyer design.

I'm a passionate gardener that requires a custom flyer design for a owner operator gardening business. Design will be for a DL flyer. I'm based on the Sunshine coast in Queensland Australia. My target audience is the residential market on the Sunshine coast. Business name is Marlowe Greens. My services are, lawn mowing, weeding, Eco Friendly fertilizing, green waste removal, Mulching, tree and shrub pruning, Full garden makeovers, hedging, pressure cleaning, privacy screening, Timber deck rejuvenation, Planting, Turf preparation and installation, and much more. Free no obligation quotes, reliable and friendly service, great rates. 12 years experience. Web www.marlowegreens.com.au - Phone 0418527064 - Email doug@marlowegreens.com.au I would like the design to portray a friendly and professional approach.

Target Market(s)

Residential

Industry/Entity Type

Gardener

Font styles to use
Serif

Colors
9ccb3b
abd037
3176b5

Requirements
Must have
• my services, my logo, my contact details,

```html
<!DOCTYPE html>
<html lang="en">
<head>
<meta charset="utf-8">
<title>Marlowe Greens – DL Flyer</title>
<link rel="stylesheet" href="https://fonts.googleapis.com/css2?family=Crimson+Text:wght@400;600;700&display=swap">
<style>
  :root {
    --lime: #abd037;
    --leaf: #9ccb3b;
    --sky: #3176b5;
    --forest: #2f6e2a;
    --ink: #15240f;
    --white: #ffffff;
    --frame: rgba(255,255,255,0.75);
  }
  * { box-sizing: border-box; margin: 0; padding: 0; }
  html, body { width: 1200px; height: 1200px; overflow: hidden; background: #fff; }
  body { position: relative; font-family: "Crimson Text", Georgia, serif; }

  .side-label {
    position: absolute; top: 600px; font-size: 13px; font-weight: 700;
    letter-spacing: 1px; color: #000; transform-origin: center;
  }
  .side-label--front { left: 2px; transform: translate(-50%, -50%) rotate(-90deg); margin-left: 20px; }
  .side-label--back { left: 1170px; transform: translate(-50%, -50%) rotate(90deg); }

  .panel {
    position: absolute; top: 27px; width: 542px; height: 1147px; overflow: hidden;
  }
  .panel__frame {
    position: absolute; inset: 19px; border: 2px solid var(--frame); z-index: 5; pointer-events: none;
  }
  .panel--front {
    left: 45px;
    background: linear-gradient(180deg, var(--lime) 0%, var(--leaf) 40%, #7fb94a 52%, #4f8f8e 80%, var(--sky) 92%, var(--sky) 100%);
  }
  .panel--back {
    left: 605px;
    background: linear-gradient(180deg, var(--sky) 0%, var(--sky) 55%, #4a8a95 66%, #7fb25c 76%, var(--leaf) 100%);
  }

  .brand {
    position: absolute; left: 0; right: 0; text-align: center; color: var(--forest);
    font-weight: 700; z-index: 3;
  }
  .brand__dot {
    display: block; margin: 0 auto 14px; border-radius: 50%; background: var(--forest);
  }
  .brand--front { top: 140px; font-size: 50px; }
  .brand--front .brand__dot { width: 120px; height: 120px; }
  .brand--back { top: 905px; font-size: 32px; }
  .brand--back .brand__dot { width: 70px; height: 70px; margin-bottom: 8px; }

  .headline {
    position: absolute; top: 472px; left: 0; right: 0; text-align: center;
    font-size: 25px; line-height: 34px; letter-spacing: 1px; color: var(--ink); z-index: 3;
  }

  .scene-photo {
    position: absolute; left: 0; right: 0; top: 455px; height: 490px;
    background:
      linear-gradient(180deg, rgba(156,203,59,0) 0%, rgba(122,184,216,0.9) 18%, rgba(118,180,210,0.7) 30%, rgba(58,120,60,0.85) 42%, rgba(70,150,70,0.9) 56%, rgba(60,140,110,0.8) 75%, rgba(49,118,181,0) 100%);
    z-index: 1;
  }

  .contact {
    position: absolute; left: 0; right: 0; text-align: center;
    font-size: 19px; line-height: 28.5px; letter-spacing: 0.3px; z-index: 3;
  }
  .contact--front { top: 1026px; color: var(--white); }
  .contact--back { top: 1028px; color: var(--ink); }

  .intro {
    position: absolute; top: 40px; left: 40px; right: 40px; text-align: center;
    color: var(--white); font-size: 15.5px; line-height: 22.5px; z-index: 3;
  }
  .intro p + p { margin-top: 7px; }

  .services__tag {
    position: absolute; top: 263px; left: 182px; width: 177px; height: 27px; border-radius: 14px;
    background: var(--lime); color: var(--sky); text-align: center; font-size: 16px; line-height: 27px;
    z-index: 3;
  }
  .services {
    position: absolute; top: 305px; left: 0; right: 0; list-style: none; text-align: center; z-index: 3;
  }
  .services li {
    color: var(--white); font-size: 16.5px; height: 28.4px; line-height: 26px; letter-spacing: 0.3px;
    position: relative;
  }
  .services li:not(:last-child)::after {
    content: ""; position: absolute; left: 100px; right: 100px; bottom: 1px; height: 2px;
    background: linear-gradient(90deg, rgba(171,208,55,0), var(--lime) 30%, var(--lime) 70%, rgba(171,208,55,0));
  }

  .badge {
    position: absolute; top: 704px; width: 128px; height: 128px; border-radius: 50%;
    background: var(--lime); border: 3px solid var(--white); color: var(--sky);
    display: flex; align-items: center; justify-content: center; text-align: center;
    font-size: 16px; line-height: 21px; z-index: 3;
  }
  .badge--quotes { left: 62px; }
  .badge--service { left: 208px; }
  .badge--rates { left: 354px; }

  .back__band {
    position: absolute; left: 0; right: 0; top: 857px; bottom: 0; background: var(--lime); z-index: 2;
  }
</style>
</head>
<body>
  <span class="side-label side-label--front">FRONT</span>
  <span class="side-label side-label--back">BACK</span>

  <section class="panel panel--front">
    <div class="panel__frame"></div>
    <div class="brand brand--front"><span class="brand__dot"></span>Marlowe Greens</div>
    <div class="scene-photo" role="img" aria-label="Photo of a lush mown lawn edged by trees and palms under a blue sky"></div>
    <h1 class="headline">A BEAUTIFUL GARDEN<br>DOESN'T HAPPEN BY ITSELF</h1>
    <div class="contact contact--front">
      <p>PHONE: 0418527064</p>
      <p>EMAIL: DOUG@MARLOWEGREENS.COM.AU</p>
      <p>WEB: WWW.MARLOWEGREENS.COM.AU</p>
    </div>
  </section>

  <section class="panel panel--back">
    <div class="panel__frame"></div>
    <div class="intro">
      <p>Marlowe Greens is your garden and lawn care specialist, with a passion for gardening and a keen eye for detail you can rest assured you're in the right hands.</p>
      <p>My services are tailored to meet every individual clients needs. From a one time mow too regular lawn mowing, all aspects of garden care and even full garden makeovers.</p>
      <p>With 12 years of experience, I go that extra mile every time to leave your garden and yard looking amazing.</p>
    </div>
    <div class="services__tag">OUR SERVICES:</div>
    <ul class="services">
      <li>LAWN MOWING</li>
      <li>WEEDING</li>
      <li>ECO FRIENDLY FERTILIZING</li>
      <li>GREEN WASTE REMOVAL</li>
      <li>MULCHING</li>
      <li>TREE AND SHRUB PRUNING</li>
      <li>FULL GARDEN MAKEOVERS</li>
      <li>HEDGING</li>
      <li>PRESSURE CLEANING</li>
      <li>PRIVACY SCREENING</li>
      <li>TIMBER DECK REJUVENATION</li>
      <li>PLANTING</li>
      <li>TURF PREPARATION AND INSTALLATION</li>
    </ul>
    <div class="badge badge--quotes">FREE<br>NO<br>OBLIGATION<br>QUOTES</div>
    <div class="badge badge--service">RELIABLE<br>AND<br>FRIENDLY<br>SERVICE</div>
    <div class="badge badge--rates">GREAT<br>RATES</div>
    <div class="back__band"></div>
    <div class="brand brand--back"><span class="brand__dot"></span>Marlowe Greens</div>
    <div class="contact contact--back">
      <p>PHONE: 0418527064</p>
      <p>EMAIL: DOUG@MARLOWEGREENS.COM.AU</p>
      <p>WEB: WWW.MARLOWEGREENS.COM.AU</p>
    </div>
  </section>
</body>
</html>
```